Business Card Design Project (Beer industry)

I am seeking a redesign of my business card. I am looking for something that will really stand out in both texture and feel. Something more on the modern side then traditional. Nothing die cut shaped like a beer mug please.

The card is used mostly for other industry professionals, as well as bar and restaurant owners. My title is Strategy & Acquisitions. If you would like to somehow incorporate that theme, that may work.

My business is craft and imported beer. Nothing fizzy and yellow, so my products are more on the upscale side.
Updates

I was able to update my logo in .ai and .tif format. I hope that helps. 

Thank you all for your creative ideas. I have uploaded my current business card in pdf format, as well as our logo in .eps file format. We are excited about the submissions so far and want to thank you all again.

PS Please do not include fax number in future submissions, as we are looking for something more creative and a fax says 1999 and not 2015, which is the message we are going for, without being futuristic. 

Thank you all once again for all of your submissions. If we would consider a two sided card, we would like the opposite side not to be the same as the front. The styles we have seen so far, it appears the front and back are too similar. Again, a two sided card is not required. Thank you and we look forward to pushing the boundaries of your creativity. Cheers

Target Market(s)

My card would mostly go to bar and restaurant operators as well as other beer industry professionals

Industry/Entity Type

Restaurant

Requirements
Nice to have
• Two sided would be considered, although not required
Should not have
• Anything die cut shaped like a beer mug.

```html
<!DOCTYPE html>
<html lang="en">
<head>
<meta charset="utf-8">
<title>Kestrel Brew – Business Card</title>
<link href="https://fonts.googleapis.com/css2?family=Questrial&family=Nunito:wght@700;900&display=swap" rel="stylesheet">
<style>
  :root {
    --paper: #ffffff;
    --navy: #1b2a6b;
    --ink-blue: #24307f;
    --wine: #7d1a14;
    --brick: #b3281f;
    --orange: #f07f1d;
  }
  * { margin: 0; padding: 0; box-sizing: border-box; }
  html, body { width: 762px; height: 1200px; overflow: hidden; background: var(--paper); }
  .card {
    position: relative;
    width: 762px;
    height: 1200px;
    background: var(--paper);
    font-family: "Questrial", sans-serif;
    color: var(--ink-blue);
  }
  .brand-art {
    position: absolute;
    left: 100px;
    top: 24px;
    width: 570px;
    height: 420px;
    border-radius: 6px;
    background: linear-gradient(180deg, #2a47b8 0%, #1f3aa8 55%, #e2a626 80%, #9c1d16 100%);
  }
  .brand-name {
    position: absolute;
    left: 0;
    top: 470px;
    width: 100%;
    text-align: center;
    font-size: 62px;
    color: var(--wine);
    letter-spacing: 1px;
  }
  .person {
    position: absolute;
    left: 0;
    top: 676px;
    width: 100%;
    text-align: center;
  }
  .person-name {
    font-family: "Nunito", sans-serif;
    font-weight: 700;
    font-size: 40px;
    color: var(--wine);
    line-height: 1.2;
  }
  .person-title { font-size: 27px; color: var(--ink-blue); margin-top: 4px; }
  .direct {
    position: absolute;
    left: 0;
    top: 822px;
    width: 100%;
    text-align: center;
    font-size: 32px;
    line-height: 52px;
  }
  .direct .label { color: var(--ink-blue); }
  .direct .cell { font-family: "Nunito", sans-serif; font-weight: 700; color: var(--wine); letter-spacing: 1px; }
  .direct .email { color: var(--brick); }
  .office {
    position: absolute;
    top: 980px;
    font-size: 29px;
    line-height: 42px;
    color: var(--ink-blue);
  }
  .office.address { left: 38px; }
  .office.phones { right: 52px; text-align: right; }
  .accent-band {
    position: absolute;
    left: 0; top: 1077px;
    width: 100%; height: 17px;
    background: var(--orange);
  }
  .footer-band {
    position: absolute;
    left: 0; top: 1098px;
    width: 100%; height: 102px;
    background: var(--navy);
    display: flex;
    align-items: center;
    justify-content: center;
  }
  .website {
    font-family: "Nunito", sans-serif;
    font-weight: 900;
    font-size: 44px;
    color: var(--brick);
    -webkit-text-stroke: 4px #ffffff;
    paint-order: stroke fill;
    letter-spacing: 0.5px;
  }
</style>
</head>
<body>
  <div class="card">
    <div class="brand-art" role="img" aria-label="Illustration of a city skyline with a statue, stars and a glass of beer with wheat"></div>
    <div class="brand-name">Kestrel Brew</div>

    <div class="person">
      <div class="person-name">Dan Okafor</div>
      <div class="person-title">Strategy &amp; Acquisitions</div>
    </div>

    <div class="direct">
      <div><span class="label">Cell: </span><span class="cell">(917) 555-0148</span></div>
      <div><span class="label">Email: </span><span class="email">dokafor@mailbox.com</span></div>
    </div>

    <div class="office address">
      <div>42 Meadow Street</div>
      <div>Brooklyn, NY 11201</div>
    </div>
    <div class="office phones">
      <div>Phone: (718) 555-0120</div>
    </div>

    <div class="accent-band"></div>
    <div class="footer-band">
      <span class="website">www.kestrelbrewusa.com</span>
    </div>
  </div>
</body>
</html>
```